We Import and supply LED Lighting products (High Bays, Flood Lights, Bulbs, Down Lights, Strip Lighting, Night Lights.) and we are after a brochure design that communicates these product points below..

1. Environmentally Friendly.
2. Recyclable
3. Energy Saving
3. Cost Savings for the customer (big and small business)
4. Long Life Span.
5. Lower Maintenance Costs.
6. Importing
7. QUALITY PRODUCTS

The brochure needs to reflect that LED lighting is a safer 'lighting' solution for the environment and also to reflect big cost savings to big and small business ... I have highlighted some colours below but will leave this to the designer to decide on.

I have included some photos that resemble the type of other LED Lighting we sell.

Kind Regards

File 3 & File 5 can't be opened so please ignore.

Target Market(s)

Industrial / Warehousing... (Highbays & Flood Lights)
Domestic: ..... Bulbs & Strip Lighting

Industry/Entity Type

Small Business

Requirements
Must have
• Your professional experience in graphic design... show me that you can produce a professional look, not just a rush job with bad spelling.

Definitely depicts that we sell Quality LED Lighting with very competitive pricing.

Wholesale and Retail.

Our Logo.. this is the image I have uploaded, '"purple circle with grey wings"
Nice to have
• images and or symbols that depict recyclable, environmentally safe. energy saving and maybe a stack of coins that show money that can be saved (especially on the highbays)
Should not have
• copying the brochure I have uploaded and just adding colour!...

```html
<!DOCTYPE html>
<html lang="en">
<head>
<meta charset="utf-8">
<title>Lumena Imports – Tri-fold Brochure</title>
<link rel="stylesheet" href="https://fonts.googleapis.com/css2?family=Arimo:wght@400;700&family=Comfortaa:wght@400;600&display=swap">
<style>
  :root{
    --page:#e4e4e0;
    --lavender:#f4e8f4;
    --cream:#f2f5e2;
    --purple:#5b2c86;
    --magenta:#c2278f;
    --green:#43ad45;
    --green-dark:#2f8a32;
    --ink:#2b2b2b;
    --white:#ffffff;
    --sky-top:#2c3f74;
    --sky-mid:#6f6a9a;
    --sky-low:#b98e6a;
  }
  *{box-sizing:border-box;margin:0;padding:0}
  html,body{width:1200px;height:1200px;overflow:hidden;background:var(--page)}
  body{font-family:"Arimo",Arial,sans-serif;color:var(--ink)}

  .brochure{
    position:absolute;left:30px;top:197px;width:1140px;height:806px;
    display:flex;box-shadow:0 6px 24px rgba(0,0,0,.18)
  }
  .panel{position:relative;width:380px;height:100%;overflow:hidden}

  /* Benefits panel */
  .panel--benefits{background:var(--lavender);padding:34px 30px 0 30px}
  .benefits__title{color:var(--purple);font-size:17px;font-weight:700;margin-bottom:14px}
  .benefits__intro,.benefit__text{font-size:12.5px;line-height:1.55;text-align:justify}
  .benefit{margin-top:16px}
  .benefit__head{display:flex;align-items:center;gap:10px;color:var(--magenta);font-weight:700;font-size:13.5px;margin-bottom:7px}
  .benefit__icon{width:22px;height:22px;flex:none}
  .benefits__product{
    position:absolute;left:30px;right:30px;bottom:0;height:150px;
    background:radial-gradient(ellipse at 55% 70%,#c9c9cf 0%,#8d8f96 30%,rgba(60,60,64,.35) 55%,rgba(244,232,244,0) 75%)
  }

  /* Contact panel */
  .panel--contact{background:var(--cream);padding:42px 34px 0 34px}
  .help__title{color:var(--purple);font-size:15px;font-weight:700;margin-bottom:14px}
  .help__text{font-size:12.5px;line-height:1.6;text-align:justify}
  .eco-badge{
    margin:52px auto 0;width:200px;height:120px;border-radius:60px 60px 22px 22px;
    background:radial-gradient(ellipse at 50% 35%,#9bd84a 0%,#4fa52e 45%,#1f6a2a 80%)
  }
  .cert-row{display:flex;justify-content:center;gap:22px;margin-top:40px}
  .cert{width:42px;height:42px;border-radius:50%;background:#6fae5a}
  .cert--square{border-radius:6px;background:#3a3a3a}
  .contact__band{position:absolute;left:0;bottom:0;width:100%;height:220px}
  .contact__text{
    position:absolute;left:0;right:0;bottom:46px;text-align:center;color:var(--white);
    font-size:13px;line-height:1.45
  }
  .contact__lead{font-weight:700;font-size:14.5px;margin-bottom:6px}

  /* Cover panel */
  .panel--cover{background:linear-gradient(#ffffff 0%,#efe8f3 12%,#d7cde6 18%)}
  .cover__brand{position:absolute;left:28px;top:30px;display:flex;align-items:center;gap:12px}
  .cover__dot{width:26px;height:26px;border-radius:50%;background:var(--purple)}
  .cover__name{font-size:21px;font-weight:700;color:var(--purple);letter-spacing:.5px}
  .cover__tagline{position:absolute;left:66px;top:62px;font-size:9.5px;color:#555}
  .cover__photo{
    position:absolute;left:0;top:100px;width:100%;height:430px;
    background:linear-gradient(180deg,var(--sky-top) 0%,#3c4f86 35%,var(--sky-mid) 62%,var(--sky-low) 88%,#7b5d45 100%)
  }
  .features{position:absolute;left:0;right:0;top:468px;display:flex;justify-content:space-around;padding:0 14px}
  .feature{display:flex;flex-direction:column;align-items:center;gap:4px;color:var(--white);font-size:8.5px;font-weight:700}
  .feature__icon{width:26px;height:26px}
  .cover__band{position:absolute;left:0;top:520px;width:100%;height:286px}
  .cover__ribbon{
    position:absolute;left:0;right:0;top:540px;text-align:center;color:var(--white);
    font-family:"Comfortaa",sans-serif;font-size:20px;letter-spacing:1px
  }
  .cover__offer{
    position:absolute;left:40px;top:620px;color:var(--white);
    font-family:"Comfortaa",sans-serif;font-size:15px;line-height:1.55
  }
</style>
</head>
<body>
<main class="brochure">

  <section class="panel panel--benefits">
    <h2 class="benefits__title">A few benefits of LED Lighting:</h2>
    <p class="benefits__intro">LED Lights are the most energy efficient lighting available today and most cost effective, they are made from non-toxic materials, generate virtually no heat and fully recyclable.</p>

    <div class="benefit">
      <h3 class="benefit__head">
        <svg class="benefit__icon" viewBox="0 0 24 24"><circle cx="12" cy="12" r="10" fill="none" stroke="#c2278f" stroke-width="2"/><path d="M7 15c2-6 6-8 10-8-1 5-4 9-10 8z" fill="#c2278f"/></svg>
        Environmentally Friendly
      </h3>
      <p class="benefit__text">LED Lights are an eco-friendly form of lighting as they do not contain mercury or other harmful gasses or emit any harmful UV rays.</p>
    </div>

    <div class="benefit">
      <h3 class="benefit__head">
        <svg class="benefit__icon" viewBox="0 0 24 24"><circle cx="12" cy="13" r="8.5" fill="none" stroke="#c2278f" stroke-width="2"/><path d="M12 8v5l3 2" fill="none" stroke="#c2278f" stroke-width="2"/><path d="M4 5l3-2M20 5l-3-2" stroke="#c2278f" stroke-width="2"/></svg>
        Long Life Span
      </h3>
      <p class="benefit__text">LED Lights have as uper long life span of 50,000 +hours considerably reducing your maintenance costs (no more blown lamp store place!)</p>
    </div>

    <div class="benefit">
      <h3 class="benefit__head">
        <svg class="benefit__icon" viewBox="0 0 24 24"><rect x="2" y="7" width="17" height="10" rx="1.5" fill="none" stroke="#c2278f" stroke-width="2"/><rect x="19" y="10" width="3" height="4" fill="#c2278f"/><rect x="4" y="9" width="8" height="6" fill="#c2278f"/></svg>
        Safety
      </h3>
      <p class="benefit__text">Most LED lights operate at low voltage so are cool to touch and much safer to handle during installation and maintenance.</p>
    </div>

    <div class="benefit">
      <h3 class="benefit__head">
        <svg class="benefit__icon" viewBox="0 0 24 24"><rect x="6" y="6" width="12" height="10" fill="#c2278f"/><rect x="3" y="10" width="3" height="3" fill="#c2278f"/><rect x="18" y="10" width="3" height="3" fill="#c2278f"/><rect x="7" y="16" width="3" height="3" fill="#c2278f"/><rect x="14" y="16" width="3" height="3" fill="#c2278f"/><rect x="9" y="9" width="2" height="2" fill="#f4e8f4"/><rect x="13" y="9" width="2" height="2" fill="#f4e8f4"/></svg>
        Insects:
      </h3>
      <p class="benefit__text">Insect attraction is greatly reduced due to minimal UV light and heat.</p>
    </div>

    <div class="benefits__product" role="img" aria-label="Product photo of small round LED deck lights with black cables"></div>
  </section>

  <section class="panel panel--contact">
    <h2 class="help__title">We are here to help:</h2>
    <p class="help__text">You may have in mind other LED products not mentioned within this brochure; simply send an email with your enquiry with as much detail as possible and we would be happy to source and quote for you.</p>

    <div class="eco-badge" role="img" aria-label="Eco friendly emblem with green leaves"></div>

    <div class="cert-row">
      <span class="cert"></span>
      <span class="cert"></span>
      <span class="cert cert--square"></span>
      <span class="cert"></span>
    </div>

    <svg class="contact__band" viewBox="0 0 380 220" preserveAspectRatio="none">
      <path d="M0 40 C120 28 260 10 380 0 L380 220 L0 220 Z" fill="var(--magenta)"/>
      <path d="M0 56 C120 44 260 26 380 16 L380 220 L0 220 Z" fill="var(--green)"/>
    </svg>
    <div class="contact__text">
      <p class="contact__lead">For all pricing and<br>quoting please contact:</p>
      <p>Daniel Brooks</p>
      <p>Mob:0400 123 456</p>
      <p>Email:sales@lumenaimports.com.au</p>
    </div>
  </section>

  <section class="panel panel--cover">
    <div class="cover__brand">
      <span class="cover__dot"></span>
      <span class="cover__name">LUMENA IMPORTS</span>
    </div>
    <p class="cover__tagline">Quality LED Products at Great Prices</p>

    <div class="cover__photo" role="img" aria-label="Photo of an illuminated curved timber shade structure by the sea at dusk"></div>

    <div class="features">
      <div class="feature">
        <svg class="feature__icon" viewBox="0 0 24 24"><circle cx="12" cy="12" r="10" fill="none" stroke="#fff" stroke-width="1.8"/><path d="M13 4l-6 10h5l-1 6 6-10h-5z" fill="#9bd84a"/></svg>
        Energy saving
      </div>
      <div class="feature">
        <svg class="feature__icon" viewBox="0 0 24 24"><path d="M12 22V10M12 12c-5 0-7-4-7-8 5 0 7 3 7 8zM12 14c5 0 7-4 7-8-5 0-7 3-7 8z" fill="#9bd84a" stroke="#9bd84a"/></svg>
        Eco-Friendly
      </div>
      <div class="feature">
        <svg class="feature__icon" viewBox="0 0 24 24"><path d="M9 3h6l-2 4c5 2 7 6 7 10 0 3-2 5-8 5s-8-2-8-5c0-4 2-8 7-10z" fill="#5fbf45"/><path d="M12 10v9M10 12h4M10 17h4" stroke="#fff" stroke-width="1.5"/></svg>
        Saving Money
      </div>
      <div class="feature">
        <svg class="feature__icon" viewBox="0 0 24 24"><path d="M12 3l4 6h-8zM4 18l4-7 3 5zM20 18l-4-7-3 5z" fill="#5fbf45"/><path d="M6 20h12" stroke="#5fbf45" stroke-width="2"/></svg>
        Recyclable
      </div>
    </div>

    <svg class="cover__band" viewBox="0 0 380 286" preserveAspectRatio="none">
      <path d="M0 14 C120 8 260 0 380 4 L380 286 L0 286 Z" fill="var(--magenta)"/>
      <path d="M0 62 C120 58 260 56 380 64 L380 286 L0 286 Z" fill="var(--green)"/>
    </svg>
    <p class="cover__ribbon">Importer &amp; Supplier</p>
    <p class="cover__offer">Quality LED Products<br>Wholesale/ Retail<br>Commercial / Domestic</p>
  </section>

</main>
</body>
</html>
```